SEAFOOD PACKAGING (Products for consumer)

We are looking to create packaging for various seafood products such as octopus and squid. We plan to sell our products in upscale supermarkets.

We are specializing in cut octopus this time.

Please include our company logo. Also, please leave a transparent area so that customers can see the product inside.
Updates

We want to show what is inside, so a picture of the octopus is not required. We need something simple and sophisticated.

Target Market(s)

upscale store in US and ASIA

Industry/Entity Type

Fisheries dealer

Requirements
Must have
• Please include the attached logo,Blue one is preferred.Please leave a transparent part so that the contents of the product can be seen by the consumer.1. product name on packaging →CUT OCTOPUS,TAKO SASHIMI,Highest quality,Top quality etc... 3. What text information should be on the packaging →(It may be edited, but this is the image) The raw materials are caught in a very clean environment and processed in a modern factory with ZEK certification. We are committed to additive-free products. 4. Packing size(cm/inch)→it will be about 19cm*22cm. 5. what kind of packaging do you use →PP or PA 6. dll →ai,jag
Nice to have
• https://quillmora.example/shots/4829174-Velka-Reef We need something simple and sophisticated like this one.
Should not have
• We want to show what is inside, so a picture of the octopus is not required. We need something simple and sophisticated.

```html
<!DOCTYPE html>
<html lang="en">
<head>
<meta charset="utf-8">
<title>Marlow Cut Octopus Packaging</title>
<link href="https://fonts.googleapis.com/css2?family=Oswald:wght@500;600&display=swap" rel="stylesheet">
<style>
  :root {
    --bg: #bdd6e6;
    --navy: #2a3f98;
    --blue: #5068a8;
    --red: #c9525a;
    --white: #f2f3f5;
    --tray: #1e1f24;
    --flesh: #c9c3cb;
  }
  * { margin: 0; padding: 0; box-sizing: border-box; }
  html, body { width: 1200px; height: 1200px; overflow: hidden; background: var(--bg); }
  body { position: relative; font-family: 'Oswald', sans-serif; }
  .pack { position: absolute; left: 213px; top: 174px; width: 742px; height: 851px; background: #dfe4ea; overflow: hidden; }
  .top-band { position: absolute; left: 0; top: 0; width: 100%; height: 50px; background: var(--navy); }
  .window { position: absolute; top: 56px; height: 600px; background: linear-gradient(90deg, var(--tray) 0%, #3a3840 20%, var(--flesh) 45%, #e6e2e8 60%, var(--flesh) 80%, var(--tray) 100%); border-radius: 14px; }
  .window.left { left: 28px; width: 166px; border-radius: 14px 0 0 14px; }
  .window.right { left: 544px; width: 166px; border-radius: 0 14px 14px 0; }
  .wave-pattern { position: absolute; left: 0; top: 610px; width: 100%; height: 241px; background: linear-gradient(180deg, #3a55ae, var(--navy)); }
  .label { position: absolute; left: 194px; top: 0; width: 350px; height: 752px; background: var(--white); }
  .brand-banner { position: absolute; left: 88px; top: 0; width: 174px; height: 279px; background: var(--blue); display: flex; align-items: flex-end; justify-content: center; padding-bottom: 40px; }
  .brand-name { color: var(--white); font-weight: 600; font-size: 40px; letter-spacing: 5px; }
  .product-name { position: absolute; left: 0; top: 368px; width: 100%; text-align: center; color: var(--red); font-weight: 600; font-size: 60px; line-height: 1; transform: scaleY(1.08); }
  .product-sub { position: absolute; left: 0; top: 432px; width: 100%; display: flex; align-items: center; justify-content: center; gap: 14px; }
  .product-sub .rule { width: 56px; height: 3px; background: var(--red); }
  .product-sub span { color: var(--blue); font-weight: 600; font-size: 34px; line-height: 1; }
  .claims { position: absolute; left: 0; top: 528px; width: 100%; height: 30px; background: var(--blue); color: var(--white); font-size: 14px; font-weight: 500; text-align: center; line-height: 30px; letter-spacing: .3px; }
  .story { position: absolute; left: 10px; top: 572px; width: 330px; text-align: center; color: var(--red); font-size: 12.5px; font-weight: 500; line-height: 17px; }
  .storage { position: absolute; left: 12px; top: 682px; display: flex; align-items: center; gap: 8px; color: var(--navy); font-size: 6.5px; font-weight: 600; line-height: 12px; }
  .cert-badge { position: absolute; left: 258px; top: 652px; width: 80px; height: 80px; border-radius: 50%; border: 3px solid var(--navy); }
  .label-waves { position: absolute; left: 0; top: 752px; width: 350px; height: 99px; }
</style>
</head>
<body>
  <div class="pack">
    <div class="top-band"></div>
    <div class="window left" role="img" aria-label="Clear window showing sliced octopus on a black tray"></div>
    <div class="window right" role="img" aria-label="Clear window showing sliced octopus on a black tray"></div>
    <div class="wave-pattern" role="img" aria-label="Blue and white seigaiha wave pattern"></div>
    <div class="label">
      <div class="brand-banner"><span class="brand-name">MARLOW</span></div>
      <h1 class="product-name">CUT OCTOPUS</h1>
      <div class="product-sub"><i class="rule"></i><span>TAKO SASHIMI</span><i class="rule"></i></div>
      <div class="claims">ALL NATURAL • HIGHEST QUALITY • TOP QUALITY</div>
      <p class="story">THE RAW MATERIALS ARE CAUGHT IN A VERY CLEAN ENVIRONMENT AND PROCESSED IN A MODERN FACTORY WITH ZEK CERTIFICATION. WE ARE COMMITTED TO ADDITIVE-FREE PRODUCTS.</p>
      <div class="storage">
        <svg width="30" height="30" viewBox="0 0 30 30" fill="none" stroke="#2a3f98" stroke-width="2" stroke-linecap="round">
          <path d="M15 2v26M3.7 8.5l22.6 13M3.7 21.5l22.6-13"/>
          <path d="M11 4l4 3 4-3M11 26l4-3 4 3M3 13l5-1-1-5M27 17l-5 1 1 5M3 17l5 1-1 5M27 13l-5-1 1-5"/>
        </svg>
        <div>KEEP FROZEN, NO PRESERVATIVES<br>NET. WT 1 LB (500 G)</div>
      </div>
      <div class="cert-badge"></div>
    </div>
    <div class="label-waves" style="left:194px; background: linear-gradient(180deg, #3a55ae, var(--navy));" role="img" aria-label="Blue and white seigaiha wave pattern"></div>
  </div>
</body>
</html>
```